Business Card - CEO

we need luxury and ultra modern business card for the CEO & Founder of two big company in fishers Indiana united state, the first company is Development company ( The Meadow Crest Group) and the other company is construction ( Tolbek Construction Group ) . we would like to see design use the color gold, white, black or dark blue. and also include the QR code and the 2 logo of the companies.

Target Market(s)

Apartment development

Industry/Entity Type

development

Contact Information for Business Card

the business card (Double-Sided) should incloud the Following: 1- Name: Karim Tolbek 2- title: CEO & Founder 3- two email: Karimtolbek@mailnest.com & CEO@themeadowcrestpark.com 4- phone # 317-555-0142. 5- website:www.themeadowcrestpark.com & www.bunyalhouse.com 6-location: Downtown Carmel Indiana. 7- slogan: The luxury of living ( free modern hand writing font style) 8- two company logo 9- QR code

Requirements
Must have
• the business card must have Double-Sided
Nice to have
• please see the example design I like is attached
Should not have
• Make sure don’t use the 2 logo on one side, just use one logo for each side

```html
<!DOCTYPE html>
<html lang="en">
<head>
<meta charset="utf-8">
<title>Karim Tolbek – Business Card</title>
<link rel="stylesheet" href="https://fonts.googleapis.com/css2?family=Josefin+Sans:wght@300&family=Montserrat:wght@400;500;800&family=Great+Vibes&display=swap">
<style>
  :root {
    --backdrop: #4a4c4f;
    --card: #2f302b;
    --gold: #c49a5c;
    --white: #f4f2ee;
  }
  * { margin: 0; padding: 0; box-sizing: border-box; }
  html, body { width: 1200px; height: 887px; overflow: hidden; }
  body {
    background: var(--backdrop);
    position: relative;
    font-family: "Montserrat", sans-serif;
  }
  .card {
    position: absolute;
    width: 540px;
    height: 310px;
    background: var(--card);
    border-radius: 26px;
    box-shadow: 0 14px 30px rgba(0,0,0,.35);
    overflow: hidden;
  }
  .card--front { left: 60px; top: 90px; }
  .card--back { left: 600px; top: 487px; }

  /* front */
  .brand-front {
    position: absolute;
    inset: 0;
    display: flex;
    flex-direction: column;
    align-items: center;
    justify-content: center;
    gap: 18px;
  }
  .brand-front__dot {
    width: 14px; height: 14px;
    border-radius: 50%;
    background: var(--gold);
  }
  .brand-front__name {
    font-family: "Josefin Sans", sans-serif;
    font-weight: 300;
    font-size: 30px;
    letter-spacing: 9px;
    text-transform: uppercase;
    color: var(--gold);
  }

  /* back */
  .brand-back {
    position: absolute;
    left: 30px; top: 92px;
    width: 196px;
    font-family: "Josefin Sans", sans-serif;
    font-weight: 300;
    font-size: 26px;
    line-height: 1.35;
    letter-spacing: 7px;
    text-transform: uppercase;
    color: var(--gold);
    text-align: center;
  }
  .divider {
    position: absolute;
    left: 238px; top: 44px;
    width: 1.5px; height: 164px;
    background: var(--gold);
  }
  .contact {
    position: absolute;
    left: 258px; top: 38px;
    color: var(--white);
  }
  .contact__name {
    font-weight: 800;
    font-size: 21px;
    color: var(--gold);
    letter-spacing: .3px;
  }
  .contact__title {
    font-size: 14px;
    margin: 2px 0 10px;
  }
  .contact__list { list-style: none; }
  .contact__item {
    display: flex;
    align-items: center;
    gap: 9px;
    font-size: 13px;
    line-height: 22px;
  }
  .contact__icon { width: 14px; height: 14px; flex: none; fill: var(--gold); }
  .footer {
    position: absolute;
    left: 0; right: 0; bottom: 20px;
    text-align: center;
    color: var(--white);
  }
  .footer__location {
    font-size: 14px;
    line-height: 22px;
  }
  .footer__slogan {
    font-family: "Great Vibes", cursive;
    font-size: 27px;
    line-height: 34px;
  }
</style>
</head>
<body>

<section class="card card--front" aria-label="Card front">
  <div class="brand-front">
    <span class="brand-front__dot"></span>
    <span class="brand-front__name">The Meadow Crest</span>
  </div>
</section>

<section class="card card--back" aria-label="Card back">
  <div class="brand-back">Tolbek Group</div>
  <div class="divider"></div>
  <div class="contact">
    <p class="contact__name">KARIM TOLBEK</p>
    <p class="contact__title">CEO &amp; Founder</p>
    <ul class="contact__list">
      <li class="contact__item">
        <svg class="contact__icon" viewBox="0 0 24 24"><path d="M6.6 10.8a15.1 15.1 0 0 0 6.6 6.6l2.2-2.2a1 1 0 0 1 1-.25 11.4 11.4 0 0 0 3.6.57 1 1 0 0 1 1 1V20a1 1 0 0 1-1 1A17 17 0 0 1 3 4a1 1 0 0 1 1-1h3.5a1 1 0 0 1 1 1c0 1.25.2 2.45.57 3.57a1 1 0 0 1-.25 1z"/></svg>
        # 317-555-0142
      </li>
      <li class="contact__item">
        <svg class="contact__icon" viewBox="0 0 24 24"><path d="M2 5h20v14H2zm2 2v.5l8 5 8-5V7z"/></svg>
        Karimtolbek@mailnest.com
      </li>
      <li class="contact__item">
        <svg class="contact__icon" viewBox="0 0 24 24"><path d="M2 5h20v14H2zm2 2v.5l8 5 8-5V7z"/></svg>
        CEO@themeadowcrestpark.com
      </li>
      <li class="contact__item">
        <svg class="contact__icon" viewBox="0 0 24 24"><path d="M12 2a10 10 0 1 0 0 20 10 10 0 0 0 0-20zm-1 17.9A8 8 0 0 1 4.1 11H7c.1 3.3 1.5 6.6 4 8.9zM7 9H4.4A8 8 0 0 1 11 4.1C8.8 6 7.3 7.4 7 9zm6 10.9c2.5-2.3 3.9-5.6 4-8.9h2.9a8 8 0 0 1-6.9 8.9zM17 9c-.3-1.6-1.8-3-4-4.9A8 8 0 0 1 19.6 9z"/></svg>
        www.themeadowcrestpark.com
      </li>
      <li class="contact__item">
        <svg class="contact__icon" viewBox="0 0 24 24"><path d="M12 2a10 10 0 1 0 0 20 10 10 0 0 0 0-20zm-1 17.9A8 8 0 0 1 4.1 11H7c.1 3.3 1.5 6.6 4 8.9zM7 9H4.4A8 8 0 0 1 11 4.1C8.8 6 7.3 7.4 7 9zm6 10.9c2.5-2.3 3.9-5.6 4-8.9h2.9a8 8 0 0 1-6.9 8.9zM17 9c-.3-1.6-1.8-3-4-4.9A8 8 0 0 1 19.6 9z"/></svg>
        www.bunyalhouse.com
      </li>
    </ul>
  </div>
  <div class="footer">
    <p class="footer__location">Downtown Carmel Indiana</p>
    <p class="footer__slogan">The luxury of living</p>
  </div>
</section>

</body>
</html>
```